Brisa Pastry Mill Business card

We are empanada whole-sellers and I want a business card design with a picture of an empanada on it that also mentions first trial order FREE. our contact number 555-214-7093 our website www.brisapastry.example and business email Tobin@brisapastry.example

If you want any of our artwork please feel free to email me at the address above.

```html
<!DOCTYPE html>
<html lang="en">
<head>
<meta charset="utf-8">
<title>Brisa Pastry Mill – Business Card</title>
<link rel="stylesheet" href="https://fonts.googleapis.com/css2?family=Libre+Baskerville:wght@400;700&display=swap">
<style>
  :root {
    --page: #ffffff;
    --mustard: #e8b321;
    --mustard-light: #efc443;
    --mustard-deep: #d9a41a;
    --ink: #141414;
    --paper: #ffffff;
    --pastry-light: #f0c98a;
    --pastry-deep: #dca05a;
  }
  html, body {
    margin: 0;
    padding: 0;
    width: 1200px;
    height: 921px;
    overflow: hidden;
    background: var(--page);
  }
  .canvas {
    position: relative;
    width: 1200px;
    height: 921px;
    font-family: "Libre Baskerville", Georgia, serif;
    color: var(--ink);
  }
  .card {
    position: absolute;
    box-sizing: border-box;
    border: 3px solid var(--ink);
    overflow: hidden;
  }
  .card-pattern {
    position: absolute;
    inset: 0;
    background: radial-gradient(circle at 50% 45%, var(--mustard-light), var(--mustard) 60%, var(--mustard-deep));
  }
  .card-back {
    left: 155px;
    top: 163px;
    width: 567px;
    height: 325px;
  }
  .card-front {
    left: 445px;
    top: 405px;
    width: 575px;
    height: 330px;
  }
  .offer {
    position: absolute;
    left: 44px;
    top: 36px;
    margin: 0;
    font-weight: 700;
    line-height: 1;
    text-shadow: 2px 2px 0 var(--paper), -1px -1px 0 var(--paper), 1px -1px 0 var(--paper), -1px 1px 0 var(--paper);
  }
  .offer span { display: block; }
  .offer-first { font-size: 42px; }
  .offer-trial { font-size: 26px; margin: 6px 0 0 46px; }
  .offer-free { font-size: 58px; margin: 4px 0 0 22px; }
  .product-art {
    position: absolute;
    left: 352px;
    top: 30px;
    width: 182px;
    height: 142px;
    border-radius: 8px;
    background: linear-gradient(160deg, var(--pastry-light), var(--pastry-deep));
  }
  .contact-panel {
    position: absolute;
    left: 40px;
    top: 194px;
    width: 490px;
    height: 92px;
    background: var(--ink);
    border-radius: 8px;
    box-sizing: border-box;
    padding: 14px 20px;
    color: var(--paper);
    font-size: 14.5px;
    font-weight: 700;
    line-height: 19px;
  }
  .contact-panel p { margin: 0; }
  .ornament {
    position: absolute;
    width: 40px;
    height: 40px;
    border-radius: 50%;
    background: var(--ink);
  }
  .ornament-top { left: 44px; top: 30px; }
  .ornament-bottom { left: 476px; top: 250px; }
  .brand {
    position: absolute;
    left: 0;
    right: 0;
    top: 100px;
    text-align: center;
  }
  .brand-name {
    margin: 0;
    font-size: 46px;
    font-weight: 700;
    line-height: 1;
    color: var(--ink);
  }
  .brand-tagline {
    margin: 24px 0 0;
    font-size: 15px;
    font-weight: 700;
    line-height: 21px;
    text-transform: uppercase;
    text-shadow: 1px 1px 0 var(--paper);
  }
</style>
</head>
<body>
<main class="canvas">
  <section class="card card-back" aria-label="Business card, offer side">
    <div class="card-pattern" role="img" aria-label="Mustard yellow background with a repeating ring pattern"></div>
    <h2 class="offer">
      <span class="offer-first">FIRST</span>
      <span class="offer-trial">TRIAL ORDER</span>
      <span class="offer-free">FREE</span>
    </h2>
    <div class="product-art" role="img" aria-label="Illustration of golden baked empanadas"></div>
    <div class="contact-panel">
      <p>555-214-7093</p>
      <p>Tobin@brisapastry.example</p>
      <p>www.brisapastry.example</p>
    </div>
  </section>

  <section class="card card-front" aria-label="Business card, brand side">
    <div class="card-pattern" role="img" aria-label="Mustard yellow background with a repeating tile pattern"></div>
    <div class="ornament ornament-top" role="img" aria-label="Black flower ornament"></div>
    <div class="brand">
      <h1 class="brand-name">Brisa Pastry Mill</h1>
      <p class="brand-tagline">Wholesale<br>Curry Puffs &amp; Empanadas</p>
    </div>
    <div class="ornament ornament-bottom" role="img" aria-label="Black flower ornament"></div>
  </section>
</main>
</body>
</html>
```